Business Card Design Project

I want a business card to give to new customers once I have finished a job. The card is to be used for referals from that customer. If they use it they receive $25 off their next bill and the new customer receives $25 off their bill. I'd like to use thye logo off my website www.tedharrowelectrical.com.au. Other colours I like are grey and red. Open to suggestions. The back of the card will have standard contact details.
Updates

Reason: Waiting on changes to the design I like.

Target Market(s)

famalies. eastern suburbs sydney.

Industry/Entity Type

Business

Requirements
Must have
• company logo. contact deatils back of card (company name, phone, website, email add.)

```html
<!DOCTYPE html>
<html lang="en">
<head>
<meta charset="utf-8">
<title>Ted Harrow Electrical – Referral Card</title>
<link rel="stylesheet" href="https://fonts.googleapis.com/css2?family=Jost:wght@400;500;700;800;900&display=swap">
<style>
  :root {
    --page: #ffffff;
    --blue-deep: #4a8fd0;
    --blue-soft: #8fb4e0;
    --blue-brand: #3f8acb;
    --blue-pale: #d3e0f0;
    --grey-light: #e6e8ec;
    --grey-mid: #b8babd;
    --grey-dark: #7b7d80;
    --red-offer: #e8402f;
    --ink: #231f20;
    --white: #ffffff;
    --text-grey: #2b2b2b;
  }
  * { margin: 0; padding: 0; box-sizing: border-box; }
  html, body {
    width: 1200px; height: 900px; overflow: hidden;
    background: var(--page);
    font-family: "Jost", "Futura", sans-serif;
  }
  .canvas { position: relative; width: 1200px; height: 900px; }
  .card { position: absolute; top: 275px; width: 573px; height: 350px; overflow: hidden; }
  .card-front { left: 17px; }
  .card-back { left: 613px; }
  .card-bg { position: absolute; inset: 0; width: 100%; height: 100%; }

  /* front */
  .brand-mark { position: absolute; left: 18px; top: 118px; display: flex; align-items: center; gap: 12px; }
  .brand-dot { width: 34px; height: 34px; border-radius: 50%; background: var(--ink); flex: none; }
  .brand-name { color: var(--white); font-weight: 800; font-size: 27px; line-height: 1.05; letter-spacing: .5px; }
  .offer { position: absolute; left: 333px; width: 200px; top: 28px; text-align: center; color: var(--red-offer); }
  .offer-lead { font-weight: 400; font-size: 38px; line-height: 40px; }
  .offer-main { font-weight: 900; font-size: 31px; line-height: 35px; }
  .call { position: absolute; right: 11px; top: 250px; text-align: right; color: var(--white); }
  .call-label { font-weight: 400; font-size: 32px; line-height: 38px; }
  .call-number { font-weight: 900; font-size: 32px; line-height: 40px; letter-spacing: 2px; }

  /* back */
  .back-title { position: absolute; left: 10px; top: 12px; font-size: 41px; line-height: 46px; color: var(--blue-brand); white-space: nowrap; }
  .back-title strong { font-weight: 900; }
  .back-title span { font-weight: 400; }
  .back-phone { position: absolute; left: 10px; top: 58px; font-weight: 900; font-size: 39px; line-height: 46px; color: var(--ink); letter-spacing: 2px; }
  .services { position: absolute; left: 10px; top: 112px; list-style: none; font-size: 19px; line-height: 26.5px; color: var(--text-grey); }
  .back-web { position: absolute; left: 10px; top: 304px; font-weight: 800; font-size: 25px; line-height: 32px; color: var(--blue-brand); }
  .ghost-mark { position: absolute; left: 268px; top: 148px; display: flex; align-items: center; gap: 10px; opacity: .55; }
  .ghost-dot { width: 30px; height: 30px; border-radius: 50%; background: var(--grey-mid); flex: none; }
  .ghost-name { color: var(--grey-dark); font-weight: 800; font-size: 27px; line-height: 1.05; }
</style>
</head>
<body>
<main class="canvas">

  <section class="card card-front" aria-label="Referral offer, front">
    <svg class="card-bg" viewBox="0 0 573 350" aria-hidden="true">
      <defs>
        <linearGradient id="blueFade" x1="0" x2="1" y1="0" y2="0">
          <stop offset="0" stop-color="#4a8fd0"/>
          <stop offset="1" stop-color="#8fb4e0"/>
        </linearGradient>
        <linearGradient id="greyFade" x1="0" x2="1" y1="0" y2="0">
          <stop offset="0" stop-color="#c9cbce"/>
          <stop offset="0.75" stop-color="#b3b5b8"/>
          <stop offset="1" stop-color="#75777a"/>
        </linearGradient>
      </defs>
      <rect width="573" height="350" fill="url(#blueFade)"/>
      <rect x="345" y="0" width="228" height="350" fill="#c3d3ea"/>
      <polygon points="100,350 573,0 573,350" fill="#ffffff"/>
      <polygon points="145,350 573,28 573,350" fill="url(#greyFade)"/>
      <polygon points="305,52 460,0 490,0 340,52" fill="#8a8c8f"/>
      <polygon points="345,15 525,15 525,172 560,172 432,238 318,172 345,172" fill="#e4e5e7" opacity=".6"/>
    </svg>
    <div class="brand-mark">
      <span class="brand-dot"></span>
      <p class="brand-name">TED HARROW<br>ELECTRICAL</p>
    </div>
    <div class="offer">
      <p class="offer-lead">RECEIVE</p>
      <p class="offer-main">25% OFF<br>YOUR<br>NEXT BILL</p>
    </div>
    <div class="call">
      <p class="call-label">Call Ted Harrow</p>
      <p class="call-number">0400 555 218</p>
    </div>
  </section>

  <section class="card card-back" aria-label="Contact details, back">
    <svg class="card-bg" viewBox="0 0 573 350" aria-hidden="true">
      <rect width="573" height="350" fill="#e6e8ec"/>
      <polygon points="200,0 573,0 573,350 470,350 250,90" fill="#d3e0f0"/>
      <polygon points="150,0 230,0 330,100 573,260 573,300 300,120" fill="#f2f4f7"/>
      <polygon points="380,350 573,200 573,230 420,350" fill="#f2f4f7"/>
    </svg>
    <div class="ghost-mark">
      <span class="ghost-dot"></span>
      <p class="ghost-name">TED HARROW<br>ELECTRICAL</p>
    </div>
    <h1 class="back-title"><strong>TED HARROW</strong> <span>ELECTRICAL</span></h1>
    <p class="back-phone">0400 555 218</p>
    <ul class="services">
      <li>residential</li>
      <li>commercial</li>
      <li>new and old</li>
      <li>lighting</li>
      <li>power</li>
      <li>phone/data/internet points</li>
      <li>and more</li>
    </ul>
    <p class="back-web">www.tedharrowelectrical.com.au</p>
  </section>

</main>
</body>
</html>
```